New Business Card Design Project

Use the flyer uploaded and website www.brightoakbuilders.com for inspiration.
List Our Services on Backside of business cards
Martin Hollis
Harborline Renovations Inc.
Licensed General Contractors
858-471-9063

Contact Information for Business Card

Use the flyer uploaded and website www.brightoakbuilders.com for inspiration. List Our Services on Backside of business cards Martin Hollis Harborline Renovations Inc. Licensed General Contractors 858-471-9063

```html
<!DOCTYPE html>
<html lang="en">
<head>
<meta charset="utf-8">
<title>Harborline Renovations – Business Card</title>
<link rel="stylesheet" href="https://fonts.googleapis.com/css2?family=Poppins:wght@400;500;800&display=swap">
<style>
  :root {
    --backdrop: #dde2e1;
    --card-black: #1e1e20;
    --brand-red: #e41e2b;
    --paper-white: #f3f4f2;
    --logo-white: #f4f4f4;
  }
  * { box-sizing: border-box; margin: 0; padding: 0; }
  html, body {
    width: 1200px; height: 925px; overflow: hidden;
    background: var(--backdrop);
    font-family: "Poppins", sans-serif;
  }
  .canvas {
    width: 1200px; height: 925px;
    display: flex; flex-direction: column;
    align-items: center; justify-content: center; gap: 56px;
  }
  .card {
    position: relative;
    width: 610px; height: 349px;
    border-radius: 28px;
    overflow: hidden;
    box-shadow: 0 10px 24px rgba(0,0,0,0.14);
  }

  /* Back side */
  .card-back { background: var(--card-black); }
  .card-back .brand-name {
    position: absolute; left: 0; right: 0; top: 128px;
    text-align: center;
    color: var(--logo-white);
    font-weight: 400; font-size: 27px; letter-spacing: 3px;
  }
  .card-back .web-band {
    position: absolute; left: 0; right: 0; top: 262px; height: 36px;
    background: var(--brand-red);
    display: flex; align-items: center; justify-content: center;
    color: #fff; font-weight: 400; font-size: 17px; letter-spacing: 4px;
  }

  /* Front side */
  .card-front { background: var(--paper-white); }
  .card-front .header-band {
    position: absolute; left: 0; right: 0; top: 0; height: 108px;
    background: var(--card-black);
    border-bottom: 5px solid var(--brand-red);
  }
  .card-front .brand-name {
    position: absolute; right: 30px; top: 40px;
    color: var(--logo-white);
    font-weight: 400; font-size: 17px; letter-spacing: 2px;
  }
  .card-front .footer-stripe {
    position: absolute; left: 0; right: 0; bottom: 0; height: 9px;
    background: var(--brand-red);
  }
  .contact {
    position: absolute; left: 46px; top: 150px;
    color: var(--brand-red);
  }
  .contact .person-name {
    font-weight: 800; font-size: 46px; line-height: 1; letter-spacing: 0.5px;
    text-transform: uppercase; margin-bottom: 14px;
  }
  .contact .detail {
    font-weight: 500; font-size: 18px; line-height: 1.45; letter-spacing: 0.5px;
  }
</style>
</head>
<body>
<main class="canvas">
  <section class="card card-back" aria-label="Business card back">
    <div class="brand-name">HARBORLINE RENOVATIONS</div>
    <div class="web-band">www.brightoakbuilders.com</div>
  </section>

  <section class="card card-front" aria-label="Business card front">
    <div class="header-band"></div>
    <div class="brand-name">HARBORLINE RENOVATIONS</div>
    <div class="contact">
      <p class="person-name">Martin Hollis</p>
      <p class="detail">Harborline Renovations Inc.</p>
      <p class="detail">Licensed General Contractors</p>
      <p class="detail">858-471-9063</p>
    </div>
    <div class="footer-stripe"></div>
  </section>
</main>
</body>
</html>
```